Out of town New Masters of Accounting

size of ad is 7” x 9.6”
please leave one inch on bottom for footer
We want to attract out of town students to join this master's in accounting program.
You DO NOT  have to use a picture of a person.
But if you do, it should be a  male with a white shirt and should not have long hair.(look like a young executive)
THE TEXT OF THE AD IS IN THE ATTACHMENTS
THE CAP LETTERS ARE THE INSTRUCTIONS

The age we are trying to attract is from 20-30 of ages.
- a clear ad .. the text should not take up the entire ad.. it should not be very crowded -
it should be an attractive ad that people would want to see and stand out
- the text very big and take up the entire ad

```html
<!DOCTYPE html>
<html lang="en">
<head>
<meta charset="utf-8">
<title>Masters of Science in Accounting – Remote Program</title>
<link rel="stylesheet" href="https://fonts.googleapis.com/css2?family=Open+Sans:wght@300;400;600;700&family=Oswald:wght@400;500&family=Alfa+Slab+One&family=Roboto+Slab:wght@700&family=Roboto:wght@400;700&display=swap">
<style>
  :root {
    --teal-deep: #0d3a4c;
    --teal: #0e5a70;
    --gold: #d39a0c;
    --orange: #f2aa1b;
    --black: #141414;
    --white: #ffffff;
    --sky: #14a7d9;
    --sky-light: #41b9e6;
    --ink: #1d1d1d;
    --page: #e8e5e0;
  }
  * { margin: 0; padding: 0; box-sizing: border-box; }
  html, body { width: 907px; height: 1200px; overflow: hidden; background: var(--page); }
  .ad {
    position: absolute; left: 11px; top: 0;
    width: 697px; height: 944px;
    transform: scale(1.27); transform-origin: 0 0;
    background: var(--white); overflow: hidden;
    font-family: "Open Sans", sans-serif;
  }
  .ad__bg { position: absolute; inset: 0; }
  .headline {
    position: absolute; left: 44px; top: 36px;
    color: var(--white); font-size: 33px; line-height: 44px; font-weight: 300;
    letter-spacing: 0.2px;
  }
  .headline strong { font-weight: 600; }
  .headline .headline__bold { font-weight: 700; }
  .headline .headline__accent { font-weight: 700; color: var(--orange); }
  .duration {
    position: absolute; left: 484px; top: 93px; width: 150px; height: 150px;
    border-radius: 50%; background: var(--black); border: 4px solid var(--white);
    display: flex; flex-direction: column; align-items: center; justify-content: center;
    font-family: "Oswald", sans-serif; text-transform: uppercase; text-align: center;
  }
  .duration__lead { color: var(--white); font-size: 18px; line-height: 22px; }
  .duration__value { color: var(--orange); font-size: 31px; line-height: 36px; font-weight: 500; }
  .remote {
    position: absolute; left: 383px; top: 312px; width: 262px; height: 152px;
    border: 2px dashed rgba(255,255,255,.8); border-bottom: none; border-radius: 14px 14px 16px 16px;
    text-align: center; color: var(--white);
  }
  .remote__flag {
    display: inline-block; margin-top: -22px; padding: 0 8px; background: var(--teal);
    font-family: "Alfa Slab One", serif; font-size: 31px; line-height: 40px; color: var(--sky-light);
  }
  .remote__text { font-size: 18px; line-height: 24px; font-weight: 600; margin-top: 2px; }
  .remote__text span { font-weight: 400; }
  .remote__facts {
    position: absolute; left: -2px; right: -2px; bottom: 0; height: 62px;
    display: flex; border-radius: 0 0 16px 16px; overflow: hidden;
  }
  .fact {
    flex: 1; background: var(--sky); display: flex; flex-direction: column;
    align-items: center; justify-content: center;
  }
  .fact + .fact { border-left: 2px solid var(--white); }
  .fact__label { font-size: 14px; line-height: 16px; }
  .fact__value { font-family: "Oswald", sans-serif; font-size: 28px; line-height: 34px; font-weight: 500; text-transform: uppercase; }
  .placement-tag {
    position: absolute; left: 413px; top: 548px; width: 290px; height: 54px;
    background: var(--white); border-radius: 12px 0 0 12px;
    box-shadow: 0 4px 0 rgba(0,0,0,.35);
    font-family: "Roboto Slab", serif; font-weight: 700; font-size: 13px; line-height: 17px;
    color: var(--ink); text-align: center; display: flex; flex-direction: column; justify-content: center;
    padding-right: 20px;
  }
  .benefits { position: absolute; left: 318px; top: 628px; display: flex; gap: 14px; }
  .benefit { width: 106px; text-align: center; }
  .benefit svg { display: block; margin: 0 auto; }
  .benefit__caption {
    margin-top: 9px; font-family: "Roboto", sans-serif; font-weight: 700;
    font-size: 12px; line-height: 15px; color: var(--ink);
  }
  .ranking { position: absolute; left: 32px; top: 742px; display: flex; align-items: center; }
  .ranking__badge { width: 56px; height: 56px; border-radius: 50%; background: var(--orange); }
  .ranking__text {
    margin-left: 16px; padding-left: 6px; border-left: 1px solid #888;
    color: var(--white); font-size: 10.5px; line-height: 13px;
  }
</style>
</head>
<body>
  <main class="ad">
    <svg class="ad__bg" width="697" height="944" viewBox="0 0 697 944" aria-hidden="true">
      <defs>
        <linearGradient id="teal-fade" x1="0" y1="0" x2="1" y2="0.4">
          <stop offset="0" stop-color="#0c3446"/>
          <stop offset="1" stop-color="#0f6680"/>
        </linearGradient>
        <clipPath id="photo-clip"><circle cx="160" cy="482" r="206"/></clipPath>
      </defs>
      <rect width="697" height="830" fill="url(#teal-fade)"/>
      <path d="M560 0 C 540 140 420 260 0 330" fill="none" stroke="rgba(255,255,255,.75)" stroke-width="1.5"/>
      <path d="M697 440 C 600 540 380 690 0 712 L0 830 L697 830 Z" fill="var(--black)"/>
      <path d="M697 462 C 600 560 380 705 0 728 L0 830 L697 830 Z" fill="var(--gold)"/>
      <path d="M0 740 C 240 800 470 812 697 812 L697 830 L0 830 Z" fill="var(--black)"/>
      <circle cx="160" cy="482" r="236" fill="var(--black)"/>
      <circle cx="160" cy="482" r="214" fill="var(--white)"/>
      <g clip-path="url(#photo-clip)" role="img" aria-label="Photo: hands typing on a laptop showing accounting charts, with a coffee cup and notebooks on a wooden desk">
        <rect x="-60" y="270" width="430" height="420" fill="#a58a6c"/>
        <rect x="-60" y="270" width="430" height="420" fill="url(#teal-fade)" opacity=".15"/>
      </g>
    </svg>

    <h1 class="headline">
      ADVANCE FURTHER<br>
      IN YOUR <strong>CAREER WITH</strong><br>
      <span class="headline__bold">A MASTERS OF SCIENCE</span><br>
      <span class="headline__accent">IN ACCOUNTING</span>
    </h1>

    <div class="duration">
      <span class="duration__lead">A Masters in only</span>
      <span class="duration__value">15 Months</span>
    </div>

    <section class="remote">
      <div class="remote__flag">All New!</div>
      <p class="remote__text"><span>Remote program</span><br>For out of town students</p>
      <div class="remote__facts">
        <div class="fact"><span class="fact__label">Course Begins</span><span class="fact__value">August 17</span></div>
        <div class="fact"><span class="fact__label">New lower</span><span class="fact__value">Prices</span></div>
      </div>
    </section>

    <div class="placement-tag">NCS/BRIGHTWAY ALLIANCE<br>JOB PLACEMENT ADVANTAGE</div>

    <ul class="benefits" style="list-style:none">
      <li class="benefit">
        <svg width="104" height="92" viewBox="0 0 104 92" aria-hidden="true">
          <polygon points="26,2 78,2 102,46 78,90 26,90 2,46" fill="none" stroke="#fff" stroke-width="3"/>
          <polygon points="30,9 74,9 95,46 74,83 30,83 9,46" fill="#fff"/>
          <polygon points="52,30 80,42 52,54 24,42" fill="var(--ink)"/>
          <path d="M36 48 v12 q16 8 32 0 v-12 l-16 7 z" fill="var(--ink)"/>
          <path d="M76 44 v14" stroke="var(--ink)" stroke-width="2"/>
        </svg>
        <p class="benefit__caption">96% placement<br>rate</p>
      </li>
      <li class="benefit">
        <svg width="104" height="92" viewBox="0 0 104 92" aria-hidden="true">
          <polygon points="26,2 78,2 102,46 78,90 26,90 2,46" fill="none" stroke="#fff" stroke-width="3"/>
          <polygon points="30,9 74,9 95,46 74,83 30,83 9,46" fill="#fff"/>
          <path d="M34 44 a18 18 0 0 1 36 0 h4 v5 h-44 v-5 z" fill="var(--ink)"/>
          <circle cx="52" cy="64" r="11" fill="none" stroke="var(--ink)" stroke-width="6" stroke-dasharray="4 3"/>
          <circle cx="52" cy="64" r="4" fill="var(--ink)"/>
        </svg>
        <p class="benefit__caption">8 placement<br>coordinators</p>
      </li>
      <li class="benefit">
        <svg width="104" height="92" viewBox="0 0 104 92" aria-hidden="true">
          <polygon points="26,2 78,2 102,46 78,90 26,90 2,46" fill="none" stroke="#fff" stroke-width="3"/>
          <polygon points="30,9 74,9 95,46 74,83 30,83 9,46" fill="#fff"/>
          <path d="M22 40 l10 -6 l14 6 l10 -4 l14 2 l12 8 l-6 6 l-18 -8 l-8 4 l16 12 l-6 6 l-12 -8 l-4 4 l-10 -6 l-12 -10 z" fill="var(--ink)"/>
        </svg>
        <p class="benefit__caption">Decades of<br>relationships<br>with 100’s<br>of firm</p>
      </li>
    </ul>

    <div class="ranking">
      <div class="ranking__badge" role="img" aria-label="Ranking badge"></div>
      <p class="ranking__text">Harwell Crest University (HCU)<br>Master in Accounting Program<br>Received the highest possible star rating</p>
    </div>
  </main>
</body>
</html>
```